Flyer für KFZ-Gutachter
Zielgruppe
NFZ und KFZ Gutachten. Firma ist neu gegründet und Flyer wird benötigt um sich bei Werkstätten, Versicherungen und Privatkunden vorzustellen.
Aufgabenstellung
Es soll elegant, klassisch sein und angelehnt sein an meine Website https://www.holvarentis.de/ Handynummer 0157 - 62830417 bitte einpflegen. Außerdem sollten die Logos des Bundesverbandes und der Zertifizierung mit im Flyer eingebunden werden. Diese lade ich hoch. Auch das korrekte Logo lade ich hoch.

```html
<!DOCTYPE html>
<html lang="de">
<head>
<meta charset="utf-8">
<title>Holvarentis Gutachten Stuttgart – Flyer</title>
<link rel="stylesheet" href="https://fonts.googleapis.com/css2?family=Tinos&family=Jost:wght@700;800&display=swap">
<style>
  :root {
    --stage: #cfcfcf;
    --dark: #333333;
    --light: #dcdcdc;
    --paper: #eeeeee;
    --ink-dark: #3a3a3a;
    --ink-light: #f2f2f2;
    --muted: #5c5c5c;
  }
  * { box-sizing: border-box; margin: 0; padding: 0; }
  html, body { width: 857px; height: 1200px; overflow: hidden; background: var(--stage); }
  .canvas { position: relative; width: 857px; height: 1200px; }
  .page { position: absolute; left: 213px; width: 430px; height: 570px; overflow: hidden; box-shadow: 0 4px 14px rgba(0,0,0,.25); }
  .page--front { top: 18px; background: var(--light); }
  .page--back { top: 612px; background: var(--light); }
  .serif { font-family: "Tinos", "Times New Roman", serif; }
  .bold-sans { font-family: "Jost", "Futura", sans-serif; font-weight: 800; }
  .abs { position: absolute; }

  /* front */
  .front-band { left: 0; top: 55px; width: 430px; height: 200px; background: var(--dark); }
  .front-intro { left: 30px; top: 105px; width: 370px; text-align: center; color: var(--ink-light); }
  .front-intro h1 { font-weight: 400; font-size: 17px; margin-bottom: 6px; }
  .front-intro .lead { font-size: 9px; margin-bottom: 14px; }
  .front-intro .copy { font-size: 9.5px; line-height: 1.3; margin-bottom: 14px; }
  .front-intro .cert { font-size: 7px; border-top: 1px solid #bbb; padding-top: 4px; width: 260px; margin: 0 auto; }
  .front-rule { left: 20px; top: 240px; width: 390px; height: 1px; background: #bbb; }
  .front-title { left: 40px; top: 300px; width: 360px; text-align: center; }
  .front-title h2 { font-weight: 400; font-size: 28px; color: var(--muted); }
  .front-title p { font-size: 9px; color: var(--ink-dark); margin-top: 2px; }
  .front-photo { left: 120px; top: 370px; width: 310px; height: 140px; background: linear-gradient(180deg,#bdbdbd 0%,#6a6a6a 55%,#2b2b2b 100%); }
  .front-foot { left: 0; top: 505px; width: 430px; height: 65px; background: var(--dark); }

  /* back */
  .back-band { left: 90px; top: 55px; width: 340px; height: 130px; background: var(--dark); }
  .back-block { left: 0; top: 250px; width: 430px; height: 320px; background: var(--dark); }
  .card { position: absolute; background: var(--paper); padding: 10px; text-align: center; }
  .card .photo { width: 100%; }
  .card h3 { font-weight: 400; font-size: 13px; color: var(--ink-dark); margin: 6px 0 3px; }
  .card p { font-size: 6.5px; line-height: 1.3; color: var(--ink-dark); }
  .card--value-a { left: 18px; top: 30px; width: 190px; }
  .card--value-a .photo { height: 120px; background: linear-gradient(135deg,#8c8c8c,#3d3d3d); }
  .card--accident { left: 220px; top: 15px; width: 190px; }
  .card--accident .photo { height: 105px; background: linear-gradient(90deg,#7a7a7a 0%,#c9c9c9 50%,#c0392b 80%); }
  .card--value-b { left: 40px; top: 255px; width: 195px; }
  .card--value-b .photo { height: 100px; background: linear-gradient(180deg,#9cb7d4 0%,#6e8c5c 45%,#2e3f7a 100%); }
  .claim { left: 250px; top: 300px; width: 170px; color: var(--ink-light); font-size: 15px; line-height: 1.25; text-align: center; }
  .team-photo { left: 275px; top: 400px; width: 130px; height: 120px; border-radius: 50%; background: radial-gradient(circle at 50% 40%,#9aa9c2,#5f6b7c); }
  .back-name { left: 40px; top: 460px; color: var(--ink-light); font-size: 14px; }
  .contact { left: 40px; top: 492px; color: var(--ink-light); font-size: 8px; line-height: 1.35; }
  .contact .gap { margin-top: 6px; }
</style>
</head>
<body>
<main class="canvas">

  <section class="page page--front">
    <div class="abs front-band"></div>
    <div class="abs front-intro serif">
      <h1>Ihr Experte für Gutachten in Stuttgart</h1>
      <p class="lead">Präzise Bewertungen für Ihre Bedürfnisse</p>
      <p class="copy">Wir sind spezialisiert auf die Erstellung von Gutachten für Nutzfahrzeuge, Kraftfahrzeugschäden und Bewertungen. Vertrauen Sie auf unsere Expertise!</p>
      <p class="cert">Sachverständige Zertifiziert nach DIN ISO/EN 17024</p>
    </div>
    <div class="abs front-rule"></div>
    <div class="abs front-title">
      <h2 class="serif">Holvarentis Gutachten Stuttgart</h2>
      <p class="bold-sans">Ihre zuverlässigen Sachverständigen vor Ort</p>
    </div>
    <div class="abs front-photo" role="img" aria-label="Schwarzweißfoto einer modernen, leeren Halle mit spiegelndem Boden"></div>
    <div class="abs front-foot"></div>
  </section>

  <section class="page page--back">
    <div class="abs back-band"></div>
    <div class="abs back-block"></div>

    <article class="card card--value-a">
      <div class="photo" role="img" aria-label="Foto eines silbernen Oldtimers mit Chromscheinwerfer"></div>
      <h3 class="serif">Wertgutachten</h3>
      <p class="bold-sans">Erhalten Sie fundierte Wertgutachten, die Ihnen bei Kaufentscheidungen oder bei der Schadenregulierung nützlich sein können.</p>
    </article>

    <article class="card card--accident">
      <div class="photo" role="img" aria-label="Foto zweier frontal zusammengestoßener Autos, grau und rot"></div>
      <h3 class="serif">Unfallgutachten</h3>
      <p class="bold-sans">Wir erstellen detaillierte Unfallgutachten, die Ihnen bei der Schadensregulierung helfen und für Versicherungen präzise nachvollziehbar sind.</p>
    </article>

    <article class="card card--value-b">
      <div class="photo" role="img" aria-label="Foto zweier Männer, die ein beschädigtes blaues Auto begutachten"></div>
      <h3 class="serif">Wertgutachten</h3>
      <p class="bold-sans">Erhalten Sie fundierte Wertgutachten, die Ihnen bei Kaufentscheidungen oder bei der Schadenregulierung nützlich sein können.</p>
    </article>

    <p class="abs claim serif">Ihre Experten<br>für präzise Gutachten.</p>
    <div class="abs team-photo" role="img" aria-label="Rundes Teamfoto zweier Sachverständiger in hellblauen Hemden"></div>
    <p class="abs back-name serif">Holvarentis Gutachten Stuttgart</p>
    <address class="abs contact bold-sans" style="font-style:normal">
      Lindenhofstr. 18<br>71642 Ludwigsburg
      <div class="gap">Telefon: 07141 - 5820374<br>E-Mail: info@holvarentis.de</div>
    </address>
  </section>

</main>
</body>
</html>
```